Broschüre für gemeinnütziges Unternehmen in den Bereichen Kunst, Kultur, Genuss und Heimatpflege
Guten Morgen Tilda am Mühlbach, lieben Dank für die schöne, flexible und rasche Arbeit! Top Kontakt! Habe den Erhalt der Daten eben bestätigt. Viele Grüße Harald Wolting
Zielgruppe
Wir kümmern uns als gemeinnützige GmbH in der Stadt Wassenberg um alles, was mit Kunst, Kultur, Genuss und Heimatpflege zu tun hat. Dafür erstellen wir immer zum Jahresende (Ende Oktober, Anfang November) eine Broschüre mit unserem Programm für das Folgejahr. Unsere Zielgruppe sind Bürgerinnen und Bürger aus dem ganzen Kreisgebiet und darüber hinaus, Altersstruktur 30plus. Der neue Look der Broschüre sollte hochwertig und modern sein.
Aufgabenstellung
Die Broschüre hat eine Klammerheftung und wird ca. 64 Seiten umfassen.
Format: 14,8 x 14,8 cm
In der Anlage an diese Anfrage befinden sich Fotos von Musterseiten, wobei 'Titelseite' die aktuelle Titelseite zeigt, 'Foto 1' eine bisherige Innenseite zeigt, 'Seite 2' und 'Seite 3/4' zeigen Musterseiten, die verdeutlichen sollen, in welche Moderene und reduzierte Richtung es gehen soll. 'Foto Übersicht' zeigt eine chronologische Übersicht. Die Broschüre soll also einen moderneren Look bekommen, gerne auch mal mit einer Doppelseite. Die Musterseiten 2 und 3/4 sind allerdings aus einer Broschüre einer Nachbarkommune, unser Heft sollte sich also davon unterscheiden.
Wichtig sind immer pro Innenseite (oder Innen-Doppelseite): Ein Foto, Titel (z.B. 'Malvina', Genre 'Live-Musik' oder 'Musik und Songnächte', Eckdaten (Datum, Uhrzeit, Location, weitere Infos), Text.
Uns wäre mit einer schön gestalteten Titelseite, sowie schön gestalteten Muster-Innenseiten (je eine Einzelseite, eine Doppelseite, eine Seite mit tabellarischer Übersicht) sehr geholfen. Wir würden dann mit der Vorlage arbeiten und die anderen Seiten 'bauen'. Wäre das ein gangbarer Weg?
Für die Titelseite kann sehr gerne Stockmaterial verwendet werden, für den Innenteil stellen wir die Fotos.
Vielleicht können Musterseiten zu 'Malvina' ('Foto 1') gestaltet werden? Das passenden Foto hängt an, es kann mit Blindtext gearbeitet werden.
Ich freue mich über ein rasches Angebot.
Ihr
Harald Wolting

```html
<!DOCTYPE html>
<html lang="de">
<head>
<meta charset="utf-8">
<title>Malvina – Musik- und Songnächte</title>
<link rel="stylesheet" href="https://fonts.googleapis.com/css2?family=Advent+Pro:wght@300;400&family=Roboto:wght@400;500&family=Roboto+Condensed:wght@600;700;800&display=swap">
<style>
  :root {
    --black: #000000;
    --white: #ffffff;
    --yellow: #ffcc00;
    --yellow-deep: #f8b900;
    --yellow-light: #ffd21a;
    --ink: #111111;
  }
  * { margin: 0; padding: 0; box-sizing: border-box; }
  html, body { width: 1200px; height: 600px; overflow: hidden; background: var(--black); }
  .spread { position: relative; width: 1200px; height: 600px; overflow: hidden; }

  /* Left page */
  .page-left { position: absolute; left: 0; top: 0; width: 600px; height: 600px; background: var(--black); overflow: hidden; }
  .hero-photo { position: absolute; left: 0; top: 84px; width: 600px; height: 516px;
    background: linear-gradient(90deg, #000 0%, #050505 35%, #3a3a3a 62%, #6a6a6a 75%, #2a2a2a 100%); }
  .hero-photo::after { content: ""; position: absolute; inset: 0;
    background: linear-gradient(180deg, rgba(0,0,0,0) 40%, rgba(0,0,0,.75) 100%); }
  .accent-shape { position: absolute; left: 0; top: 0; width: 600px; height: 600px; }

  .genre-tag { position: absolute; left: 0; top: 0; width: 600px; height: 50px; }
  .genre-tag-text { position: absolute; left: 351px; top: 6px; font-family: "Advent Pro", sans-serif;
    font-weight: 400; font-size: 19px; letter-spacing: .5px; color: var(--ink); }

  .event-title { position: absolute; left: 41px; top: 168px; font-family: "Advent Pro", sans-serif;
    font-weight: 300; font-size: 66px; letter-spacing: 3px; line-height: 1; color: var(--white); }
  .event-text { position: absolute; left: 43px; top: 244px; width: 355px; font-family: "Roboto", sans-serif;
    font-size: 14.3px; line-height: 21.4px; color: var(--white); }
  .event-facts { position: absolute; left: 43px; top: 428px; font-family: "Advent Pro", sans-serif;
    font-weight: 400; font-size: 30px; line-height: 36px; letter-spacing: .5px; color: var(--white); }
  .event-facts .highlight { color: var(--yellow); }
  .reservation { position: absolute; left: 43px; top: 556px; font-family: "Roboto", sans-serif;
    font-size: 12.5px; color: var(--white); }

  /* Right page */
  .page-right { position: absolute; left: 600px; top: 0; width: 600px; height: 600px; background: var(--yellow); overflow: hidden; }
  .page-right svg { position: absolute; inset: 0; }
  .month { position: absolute; left: 41px; top: 49px; font-family: "Roboto Condensed", sans-serif;
    font-weight: 800; font-size: 36px; letter-spacing: 1px; color: var(--ink); }
  .program-item { position: absolute; width: 236px; font-family: "Roboto", sans-serif; color: var(--ink); }
  .program-item h3 { font-family: "Roboto Condensed", sans-serif; font-weight: 700; font-size: 23px;
    letter-spacing: .3px; line-height: 26px; }
  .program-item p { font-size: 14.2px; line-height: 17.5px; margin-top: 2px; }
  .program-item.loose p { line-height: 22.5px; }
  .divider { position: absolute; width: 236px; height: 1.5px; background: var(--ink); }
</style>
</head>
<body>
<main class="spread">
  <section class="page-left">
    <div class="hero-photo" role="img" aria-label="Schwarzweißfoto der Sängerin Malvina, Blick nach oben, Hände am Kopf"></div>
    <svg class="accent-shape" viewBox="0 0 600 600" aria-hidden="true">
      <polygon points="360,203 392,203 542,484 520,600 355,600 365,420" fill="#ffcc00" opacity=".72"/>
    </svg>
    <svg class="genre-tag" viewBox="0 0 600 50" aria-hidden="true">
      <polygon points="341,0 557,0 557,32 330,43" fill="#ffcc00"/>
    </svg>
    <div class="genre-tag-text">MUSIK- UND SONGNÄCHTE</div>

    <h1 class="event-title">MALVINA</h1>
    <p class="event-text">Lorem ipsum dolor sit amet, consectetuer adipiscing elit. Aenean commodo ligula eget dolor. Aenean massa. Cum sociis natoque penatibus et magnis dis parturient montes, nascetur ridiculus mus. Donec quam felis, ultricies nec, pellentesque eu, pretium quis, sem. Nulla consequat massa quis enim. Aenean commodo ligula eget dolor. Aenean massa. Cum sociis natoque</p>
    <div class="event-facts">
      <div class="highlight">17. MAI</div>
      <div>MI&nbsp; 20 UHR | BERFRIED</div>
      <div class="highlight">EINTRITT FREI</div>
    </div>
    <p class="reservation">Reservierung unter: www.lindenau-erleben.de</p>
  </section>

  <section class="page-right">
    <svg viewBox="0 0 600 600" aria-hidden="true">
      <polygon points="371,0 600,0 600,600 510,600 300,440 200,160" fill="#f8b900"/>
      <polygon points="505,0 600,0 600,180 420,420" fill="#ffd21a" opacity=".8"/>
      <polygon points="0,460 100,520 95,600 0,600" fill="#f8b900"/>
      <polygon points="300,440 510,600 330,600" fill="#fbc000"/>
    </svg>
    <h2 class="month">OKTOBER 2024</h2>

    <article class="program-item" style="left:41px;top:113px">
      <h3>VERANSTALTUNG 01</h3>
      <p>Lorem ipsum dolor sit amet,<br>consectetuer adipiscing elit.</p>
    </article>
    <div class="divider" style="left:42px;top:187px"></div>
    <article class="program-item" style="left:41px;top:201px">
      <h3>VERANSTALTUNG 03</h3>
      <p>Lorem ipsum dolor sit amet,<br>consectetuer adipiscing elit.</p>
    </article>
    <div class="divider" style="left:42px;top:275px"></div>
    <article class="program-item" style="left:41px;top:286px">
      <h3>VERANSTALTUNG 05</h3>
      <p>Lorem ipsum dolor sit amet,<br>consectetuer adipiscing elit.</p>
    </article>
    <div class="divider" style="left:42px;top:365px"></div>
    <article class="program-item loose" style="left:41px;top:379px">
      <h3>VERANSTALTUNG 06</h3>
      <p>Lorem ipsum dolor sit amet,<br>consectetuer adipiscing elit.</p>
    </article>

    <article class="program-item" style="left:312px;top:147px">
      <h3>VERANSTALTUNG 02</h3>
      <p>Lorem ipsum dolor sit amet,<br>consectetuer adipiscing elit.</p>
    </article>
    <div class="divider" style="left:313px;top:223px"></div>
    <article class="program-item" style="left:312px;top:235px">
      <h3>VERANSTALTUNG 04</h3>
      <p>Lorem ipsum dolor sit amet,<br>consectetuer adipiscing elit.</p>
    </article>
    <div class="divider" style="left:313px;top:312px"></div>
    <article class="program-item" style="left:312px;top:323px">
      <h3>VERANSTALTUNG 06</h3>
      <p>Lorem ipsum dolor sit amet,<br>consectetuer adipiscing elit.</p>
    </article>
    <div class="divider" style="left:313px;top:400px"></div>
    <article class="program-item" style="left:312px;top:411px">
      <h3>VERANSTALTUNG 08</h3>
      <p>Lorem ipsum dolor sit amet,<br>consectetuer adipiscing elit.</p>
    </article>
  </section>
</main>
</body>
</html>
```